Finance web application design

We need a design for a new responsive finance web application. It should look uber professional and modern.

Inspiration and design we like:

website:
http://www.halverstone.com/

The application presented here:
http://financial.marrowgate.com/en/products/tools-applications/trading-investment-tools/vexla-trading-software.html

https://apps.pindlewick.com/us/app/kestrovan-for-tabrix/id582019346?mt=8

The application presented here (Tabrix version):
https://apps.pindlewick.com/en/app/zumik-forex-trading/id481033866?mt=8&utm_source=zumikButton

Target Market(s)

Private Investors

Industry/Entity Type

Finance

Number of Pages Required

5+ page

Font styles to use
Other font styles liked:
• Nobile

Requirements
Must have
• Colors for "up" changes: green
• Colors for "down" changes: red
• Fonts in tables must be very easy to read -
• Deliver design for all pages attached.
Nice to have
• A dark (gray) background
• Graphs should be shaded and partly transparent - orange or blue
• White text as "normal" - orange text / blue text for headers
Should not have
• White background

```html
<!DOCTYPE html>
<html lang="en">
<head>
<meta charset="utf-8">
<title>Ledgerwise – Strategy</title>
<link rel="stylesheet" href="https://fonts.googleapis.com/css2?family=Nobile:wght@400;700&family=Fira+Sans:wght@400;500;600&display=swap">
<style>
:root{
  --page:#2e3539;
  --bar:#1e2225;
  --bar-line:#353c40;
  --panel:#1f1f1f;
  --panel-alt:#191919;
  --panel-head-top:#2b2b2b;
  --panel-head-bottom:#222;
  --panel-edge:#3c4448;
  --grid:#2c2c2c;
  --text:#ffffff;
  --muted:#8a9196;
  --label:#9aa1a6;
  --accent:#4fc3ea;
  --area:#3a7f9d;
  --orange:#f0952a;
  --up:#6cc24a;
  --down:#e0533f;
}
*{box-sizing:border-box;margin:0;padding:0}
html,body{width:1200px;height:2344px;overflow:hidden}
body{background:var(--page);color:var(--text);font-family:"Fira Sans",Arial,sans-serif;position:relative}
.abs{position:absolute}

/* top bar */
.topbar{left:0;top:0;width:1200px;height:66px;background:var(--bar);border-bottom:1px solid #15191b}
.brand{left:52px;top:17px;display:flex;align-items:center;gap:8px;font-family:"Nobile",sans-serif;font-weight:700;font-size:25px;color:var(--orange)}
.brand-dot{width:12px;height:12px;background:var(--orange)}
.nav{left:258px;top:0;height:66px;display:flex}
.nav a{display:flex;align-items:center;justify-content:center;height:66px;color:var(--text);text-decoration:none;font-size:13px;border-left:1px solid var(--bar-line)}
.nav a:last-child{border-right:1px solid var(--bar-line)}
.search{left:800px;top:17px;width:245px;height:33px;background:#fff;border-radius:2px;display:flex;align-items:center;justify-content:space-between;padding:0 12px;font-size:12px;color:#8a8a8a}
.user-sep{left:1066px;top:0;width:1px;height:66px;background:var(--bar-line)}
.avatar{left:1081px;top:14px;width:33px;height:33px;background:linear-gradient(#b08868,#6f5a48);border:1px solid #555}
.user{left:1122px;top:14px;font-size:13px;line-height:17px}
.user b{font-weight:600;display:block}
.user a{color:var(--accent);text-decoration:none;font-size:12px}

/* titles */
.crumb{left:52px;top:99px;font-style:italic;font-size:16px;color:#aab0b4}
.section-title{font-family:"Nobile",sans-serif;font-weight:700;font-size:24px;line-height:30px;color:var(--text)}

/* data tables */
.data{border-collapse:collapse;table-layout:fixed;background:var(--panel);box-shadow:0 0 0 1px var(--panel-edge)}
.data th{height:50px;background:linear-gradient(var(--panel-head-top),var(--panel-head-bottom));color:var(--muted);font-weight:500;font-size:12.5px;border-bottom:1px solid #111}
.data td{height:47px;font-size:12.5px;font-weight:500;color:var(--text)}
.data tbody tr:nth-child(even) td{background:var(--panel-alt)}
.data .left{text-align:left;padding-left:21px}
.data .center{text-align:center}
.up{color:var(--up)!important}
.down{color:var(--down)!important}
.sort{display:inline-block;vertical-align:middle;margin-left:4px}

.returns{left:52px;top:206px;width:1096px}
.returns td{font-size:12px}

.kpis{left:800px;top:489px;width:352px}
.kpis td{height:50px;font-size:12px}
.kpis th:first-child,.kpis td:first-child{padding-left:27px;text-align:left}
.kpis th:last-child{text-align:left;padding-left:4px}
.kpis td:last-child{text-align:right;padding-right:21px}

.positions{left:52px;top:2016px;width:1096px}

.chart text{font-family:"Fira Sans",sans-serif;font-size:11.5px;fill:var(--label)}
.chart .y{text-anchor:end}
.chart .x{text-anchor:middle}

.all-trades{left:1011px;top:1980px;font-size:12px;font-weight:500;color:var(--accent);text-decoration:underline;letter-spacing:.3px}
.due{right:52px;top:2230px;font-size:18px;color:var(--text)}
</style>
</head>
<body>

<header class="topbar abs">
  <div class="brand abs"><span class="brand-dot"></span>Ledgerwise</div>
  <nav class="nav abs">
    <a href="#" style="width:94px">Dashboard</a>
    <a href="#" style="width:78px">Strategies</a>
    <a href="#" style="width:86px">Portfolios</a>
    <a href="#" style="width:132px">Market Data</a>
    <a href="#" style="width:63px">Cust Inst.</a>
    <a href="#" style="width:70px">Users</a>
  </nav>
  <div class="search abs"><span>Search ...</span>
    <svg width="12" height="12" viewBox="0 0 12 12"><circle cx="5" cy="5" r="3.6" fill="none" stroke="#333" stroke-width="1.6"/><line x1="7.6" y1="7.6" x2="11" y2="11" stroke="#333" stroke-width="1.8"/></svg>
  </div>
  <div class="user-sep abs"></div>
  <div class="avatar abs" role="img" aria-label="User profile photo"></div>
  <div class="user abs"><b>John Doe</b><a href="#">Sign out</a></div>
</header>

<div class="crumb abs">Strategy Name</div>
<h2 class="section-title abs" style="left:52px;top:158px">Statistics</h2>

<table class="data returns abs">
  <colgroup><col style="width:96px"><col span="12" style="width:73.08px"><col style="width:123px"></colgroup>
  <thead><tr>
    <th class="left">Year<svg class="sort" width="6" height="10" viewBox="0 0 6 10"><path d="M3 0L6 4H0z M3 10L0 6H6z" fill="#8a9196"/></svg></th>
    <th>Jan</th><th>Feb</th><th>Mar</th><th>Apr</th><th>May</th><th>June</th><th>July</th><th>Aug</th><th>Sept</th><th>Oct</th><th>Nov</th><th>Dec</th><th>Compound</th>
  </tr></thead>
  <tbody class="center">
    <tr><td class="left">2012</td><td class="center">-0.04%</td><td class="center">-0.04%</td><td class="center">-0.04%</td><td class="center up">-0.04%</td><td class="center down">-0.04%</td><td class="center down">-0.04%</td><td class="center up">-0.04%</td><td class="center">-0.04%</td><td class="center up">-0.04%</td><td class="center">-0.04%</td><td class="center">-0.04%</td><td class="center">-0.04%</td><td class="center">-0.04%</td></tr>
    <tr><td class="left">2013</td><td class="center">-0.04%</td><td class="center">-0.04%</td><td class="center">-0.04%</td><td class="center">-0.04%</td><td class="center">-0.04%</td><td class="center">-0.04%</td><td class="center">-0.04%</td><td class="center">-0.04%</td><td class="center">-0.04%</td><td class="center">-0.04%</td><td class="center">-0.04%</td><td class="center">-0.04%</td><td class="center">-0.04%</td></tr>
    <tr><td class="left">2014</td><td class="center">-0.04%</td><td class="center">-0.04%</td><td class="center">-0.04%</td><td class="center">-0.04%</td><td class="center">-0.04%</td><td class="center">-0.04%</td><td class="center">-0.04%</td><td class="center">-0.04%</td><td class="center">-0.04%</td><td class="center">-0.04%</td><td class="center">-0.04%</td><td class="center">-0.04%</td><td class="center">-0.04%</td></tr>
  </tbody>
</table>

<h2 class="section-title abs" style="left:52px;top:443px">Equity Curve</h2>
<svg class="chart abs" style="left:52px;top:480px" width="740" height="330" viewBox="52 480 740 330">
  <rect x="144" y="489" width="626" height="284" fill="var(--panel)" stroke="var(--panel-edge)" stroke-width="2"/>
  <g stroke="var(--grid)" stroke-width="1">
    <line x1="145" y1="534" x2="769" y2="534"/><line x1="145" y1="583" x2="769" y2="583"/><line x1="145" y1="630" x2="769" y2="630"/><line x1="145" y1="677" x2="769" y2="677"/><line x1="145" y1="723" x2="769" y2="723"/>
  </g>
  <path d="M145 753L252 706L355 602L458 695L563 675L667 730L770 698L770 773L145 773Z" fill="var(--area)" fill-opacity=".9"/>
  <polyline points="145,753 252,706 355,602 458,695 563,675 667,730 770,698" fill="none" stroke="var(--accent)" stroke-width="2"/>
  <g fill="#fff" stroke="var(--accent)" stroke-width="2">
    <circle cx="145" cy="753" r="7"/><circle cx="252" cy="706" r="7"/><circle cx="355" cy="602" r="7"/><circle cx="458" cy="695" r="7"/><circle cx="563" cy="675" r="7"/><circle cx="667" cy="730" r="7"/><circle cx="770" cy="698" r="7"/>
  </g>
  <g class="y"><text x="118" y="538">2500000</text><text x="118" y="587">2000000</text><text x="118" y="634">1500000</text><text x="118" y="681">1000000</text><text x="118" y="727">500000</text><text x="118" y="774">0</text></g>
  <g class="x"><text x="173" y="796">Jan</text><text x="223" y="796">Feb</text><text x="273" y="796">Mar</text><text x="325" y="796">Apr</text><text x="377" y="796">May</text><text x="430" y="796">June</text><text x="483" y="796">July</text><text x="534" y="796">Aug</text><text x="588" y="796">Sept</text><text x="641" y="796">Oct</text><text x="691" y="796">Nov</text><text x="742" y="796">Dec</text></g>
</svg>

<h2 class="section-title abs" style="left:52px;top:866px">Drawdown</h2>
<svg class="chart abs" style="left:52px;top:902px" width="740" height="320" viewBox="52 902 740 320">
  <rect x="144" y="911" width="626" height="284" fill="var(--panel)" stroke="var(--panel-edge)" stroke-width="2"/>
  <g stroke="var(--grid)" stroke-width="1">
    <line x1="145" y1="958" x2="769" y2="958"/><line x1="145" y1="1005" x2="769" y2="1005"/><line x1="145" y1="1052" x2="769" y2="1052"/><line x1="145" y1="1098" x2="769" y2="1098"/><line x1="145" y1="1145" x2="769" y2="1145"/>
  </g>
  <path d="M145 912L770 912L770 986L667 955L563 1009L458 989L355 1083L250 978L145 931Z" fill="var(--area)" fill-opacity=".9"/>
  <polyline points="145,931 250,978 355,1083 458,989 563,1009 667,955 770,986" fill="none" stroke="var(--accent)" stroke-width="2"/>
  <g fill="#fff" stroke="var(--accent)" stroke-width="2">
    <circle cx="145" cy="931" r="7"/><circle cx="250" cy="978" r="7"/><circle cx="355" cy="1083" r="7"/><circle cx="458" cy="989" r="7"/><circle cx="563" cy="1009" r="7"/><circle cx="667" cy="955" r="7"/><circle cx="770" cy="986" r="7"/>
  </g>
  <g class="y"><text x="118" y="962">2500000</text><text x="118" y="1009">2000000</text><text x="118" y="1056">1500000</text><text x="118" y="1102">1000000</text><text x="118" y="1149">500000</text><text x="118" y="1196">0</text></g>
  <g class="x"><text x="173" y="1218">Jan</text><text x="223" y="1218">Feb</text><text x="273" y="1218">Mar</text><text x="325" y="1218">Apr</text><text x="377" y="1218">May</text><text x="430" y="1218">June</text><text x="483" y="1218">July</text><text x="534" y="1218">Aug</text><text x="588" y="1218">Sept</text><text x="641" y="1218">Oct</text><text x="691" y="1218">Nov</text><text x="742" y="1218">Dec</text></g>
</svg>

<h2 class="section-title abs" style="left:52px;top:1263px">Market Timing</h2>
<svg class="chart abs" style="left:52px;top:1305px" width="740" height="270" viewBox="52 1305 740 270">
  <rect x="144" y="1313" width="626" height="226" fill="var(--panel)" stroke="var(--panel-edge)" stroke-width="2"/>
  <g stroke="var(--grid)" stroke-width="1">
    <line x1="145" y1="1348" x2="769" y2="1348"/><line x1="145" y1="1388" x2="769" y2="1388"/><line x1="145" y1="1428" x2="769" y2="1428"/><line x1="145" y1="1468" x2="769" y2="1468"/><line x1="145" y1="1508" x2="769" y2="1508"/>
  </g>
  <g fill="var(--accent)">
    <rect x="170" y="1495" width="7" height="44"/><rect x="220" y="1464" width="7" height="75"/><rect x="270" y="1430" width="7" height="109"/><rect x="322" y="1419" width="7" height="120"/><rect x="374" y="1430" width="7" height="109"/><rect x="427" y="1478" width="7" height="61"/><rect x="480" y="1409" width="7" height="130"/><rect x="531" y="1419" width="7" height="120"/><rect x="585" y="1359" width="7" height="180"/><rect x="638" y="1389" width="7" height="150"/><rect x="688" y="1425" width="7" height="114"/><rect x="739" y="1359" width="7" height="180"/>
  </g>
  <g class="y"><text x="130" y="1352">1</text><text x="130" y="1540">0</text></g>
  <g class="x"><text x="173" y="1567">Jan</text><text x="223" y="1567">Feb</text><text x="273" y="1567">Mar</text><text x="325" y="1567">Apr</text><text x="377" y="1567">May</text><text x="430" y="1567">June</text><text x="483" y="1567">July</text><text x="534" y="1567">Aug</text><text x="588" y="1567">Sept</text><text x="641" y="1567">Oct</text><text x="691" y="1567">Nov</text><text x="742" y="1567">Dec</text></g>
</svg>

<h2 class="section-title abs" style="left:52px;top:1615px">Number of Instruments Passing Filter</h2>
<svg class="chart abs" style="left:52px;top:1655px" width="740" height="270" viewBox="52 1655 740 270">
  <rect x="144" y="1663" width="626" height="226" fill="var(--panel)" stroke="var(--panel-edge)" stroke-width="2"/>
  <g stroke="var(--grid)" stroke-width="1">
    <line x1="145" y1="1700" x2="769" y2="1700"/><line x1="145" y1="1738" x2="769" y2="1738"/><line x1="145" y1="1775" x2="769" y2="1775"/><line x1="145" y1="1813" x2="769" y2="1813"/><line x1="145" y1="1850" x2="769" y2="1850"/>
  </g>
  <g fill="var(--accent)">
    <rect x="170" y="1845" width="7" height="44"/><rect x="220" y="1814" width="7" height="75"/><rect x="270" y="1781" width="7" height="108"/><rect x="322" y="1770" width="7" height="119"/><rect x="374" y="1781" width="7" height="108"/><rect x="427" y="1830" width="7" height="59"/><rect x="480" y="1739" width="7" height="150"/><rect x="531" y="1770" width="7" height="119"/><rect x="585" y="1711" width="7" height="178"/><rect x="638" y="1739" width="7" height="150"/><rect x="688" y="1777" width="7" height="112"/><rect x="739" y="1711" width="7" height="178"/>
  </g>
  <g class="y"><text x="130" y="1704">5</text><text x="130" y="1742">4</text><text x="130" y="1779">3</text><text x="130" y="1817">2</text><text x="130" y="1854">1</text><text x="130" y="1892">0</text></g>
  <g class="x"><text x="173" y="1918">Jan</text><text x="223" y="1918">Feb</text><text x="273" y="1918">Mar</text><text x="325" y="1918">Apr</text><text x="377" y="1918">May</text><text x="430" y="1918">June</text><text x="483" y="1918">July</text><text x="534" y="1918">Aug</text><text x="588" y="1918">Sept</text><text x="641" y="1918">Oct</text><text x="691" y="1918">Nov</text><text x="742" y="1918">Dec</text></g>
</svg>

<h2 class="section-title abs" style="left:802px;top:443px">Statistics</h2>
<table class="data kpis abs">
  <colgroup><col style="width:212px"><col style="width:140px"></colgroup>
  <thead><tr><th>Name</th><th>Value</th></tr></thead>
  <tbody>
    <tr><td>CommissionCARGImpact</td><td>1.000.000 NOK</td></tr>
    <tr><td>CommissionCARGImpact</td><td>1.000.000 NOK</td></tr>
    <tr><td>CommissionCARGImpact</td><td>1.000.000 NOK</td></tr>
    <tr><td>CommissionCARGImpact</td><td>1.000.000 NOK</td></tr>
    <tr><td>CommissionCARGImpact</td><td>1.000.000 NOK</td></tr>
    <tr><td>CommissionCARGImpact</td><td>1.000.000 NOK</td></tr>
    <tr><td>CommissionCARGImpact</td><td>1.000.000 NOK</td></tr>
    <tr><td>CommissionCARGImpact</td><td>1.000.000 NOK</td></tr>
    <tr><td>CommissionCARGImpact</td><td>1.000.000 NOK</td></tr>
    <tr><td>CommissionCARGImpact</td><td>1.000.000 NOK</td></tr>
    <tr><td>CommissionCARGImpact</td><td>1.000.000 NOK</td></tr>
    <tr><td>CommissionCARGImpact</td><td>1.000.000 NOK</td></tr>
    <tr><td>CommissionCARGImpact</td><td>1.000.000 NOK</td></tr>
    <tr><td>CommissionCARGImpact</td><td>1.000.000 NOK</td></tr>
    <tr><td>CommissionCARGImpact</td><td>1.000.000 NOK</td></tr>
    <tr><td>CommissionCARGImpact</td><td>1.000.000 NOK</td></tr>
    <tr><td>CommissionCARGImpact</td><td>1.000.000 NOK</td></tr>
    <tr><td>CommissionCARGImpact</td><td>1.000.000 NOK</td></tr>
    <tr><td>CommissionCARGImpact</td><td>1.000.000 NOK</td></tr>
  </tbody>
</table>

<h2 class="section-title abs" style="left:52px;top:1969px">Open Positions</h2>
<a class="all-trades abs" href="#">VIEW ALL TRADES</a>
<table class="data positions abs">
  <colgroup><col style="width:560px"><col style="width:180px"><col style="width:170px"><col style="width:186px"></colgroup>
  <thead><tr>
    <th class="left">Name<svg class="sort" width="6" height="10" viewBox="0 0 6 10"><path d="M3 0L6 4H0z M3 10L0 6H6z" fill="#8a9196"/></svg></th>
    <th class="left" style="padding-left:41px">ID</th><th class="left" style="padding-left:22px">Quantity</th><th class="left" style="padding-left:46px">Date</th>
  </tr></thead>
  <tbody>
    <tr><td class="left">Holgberg Rurik</td><td class="left" style="padding-left:41px">XFIN8AX</td><td class="left" style="padding-left:27px">123.23</td><td class="left" style="padding-left:43px">12/15/2014</td></tr>
    <tr><td class="left">Holgberg Rurik</td><td class="left" style="padding-left:41px">XFIN8AX</td><td class="left" style="padding-left:27px">123.23</td><td class="left" style="padding-left:43px">12/15/2014</td></tr>
    <tr><td class="left">Holgberg Rurik</td><td class="left" style="padding-left:41px">XFIN8AX</td><td class="left" style="padding-left:27px">123.23</td><td class="left" style="padding-left:43px">12/15/2014</td></tr>
  </tbody>
</table>

<p class="due abs">New positions due on &nbsp;EOD 12/31/2014</p>

</body>
</html>
```